The Amber Lantern illustrated story adaptation design

I need a graphic-novel-style design of the 10-page story, “The Amber Lantern.” This will appear in a collection of graphic-novel-style adaptations of stories which I am posting online (and printing) in May.

Half of the files are on filecrate (under "6 images"):

https://www.filecrate-share.net/s/q3mz81kd0tx5pw2/page%20thumbs_0full_01.jpg?dl=0

Target Market(s)

comic book readers, graphic novel readers, young adult readers

Industry/Entity Type

Publishing

Font styles to use
Serif
Other font styles liked:
• Caslon Anitque, Californian FB, 1584 Pragmatica Lima

Colors

Designer to choose colors to be used in the design.

Requirements
Must have
• A bold design scheme !! The art and text are solid, but they certainly need a clever design concept that can bind the project together.
Nice to have
• An inviting, reader-friendly background of some kind (I offer suggestions in my notes).
Should not have
• Hard-to-read graphics

```html
<!DOCTYPE html>
<html lang="en">
<head>
<meta charset="utf-8">
<title>The Amber Lantern — Page 3</title>
<link href="https://fonts.googleapis.com/css2?family=Crimson+Pro:wght@700&family=Libre+Baskerville:wght@400;700&display=swap" rel="stylesheet">
<style>
  :root {
    --paper-white: #ffffff;
    --wall-olive: #8a8452;
    --wall-olive-light: #b3ad7c;
    --wall-olive-dark: #5f5b33;
    --wall-teal: #6f8a7e;
    --wall-moss: #4f6a4c;
    --wall-pale: #c9c6ae;
    --frame-black: #0b0b0b;
    --parchment: #e4dfc8;
    --parchment-light: #efeadb;
    --parchment-shade: #cfc9b0;
    --parchment-teal: #b9c2b1;
    --ink: #18150f;
    --header-ink: #f6f2e4;
    --scene-indigo: #2f2c86;
    --scene-violet: #4b2f96;
    --scene-magenta: #d4267f;
    --scene-rose: #8e2a7a;
    --scene-navy: #1b1d58;
    --scene-slate: #3f4aa0;
  }
  * { box-sizing: border-box; margin: 0; padding: 0; }
  html, body {
    width: 1200px; height: 1200px; overflow: hidden;
    background: var(--paper-white);
  }
  .page {
    position: absolute; left: 172px; top: 68px; width: 856px; height: 1064px;
    overflow: hidden;
    background:
      radial-gradient(ellipse 180px 60px at 20% 6%, var(--wall-pale), transparent 70%),
      radial-gradient(ellipse 120px 90px at 70% 12%, var(--wall-teal), transparent 70%),
      radial-gradient(ellipse 160px 110px at 8% 30%, var(--wall-olive-light), transparent 70%),
      radial-gradient(ellipse 260px 40px at 60% 52%, var(--wall-moss), transparent 75%),
      radial-gradient(ellipse 300px 30px at 55% 61%, var(--wall-teal), transparent 75%),
      radial-gradient(ellipse 90px 160px at 4% 62%, var(--wall-pale), transparent 70%),
      radial-gradient(ellipse 140px 120px at 96% 45%, var(--wall-olive-light), transparent 70%),
      radial-gradient(ellipse 200px 120px at 12% 88%, var(--wall-teal), transparent 70%),
      radial-gradient(ellipse 220px 80px at 70% 98%, var(--wall-olive-light), transparent 70%),
      radial-gradient(ellipse 120px 80px at 40% 24%, var(--wall-olive-dark), transparent 70%),
      radial-gradient(ellipse 160px 100px at 85% 80%, var(--wall-olive-dark), transparent 70%),
      linear-gradient(180deg, var(--wall-olive) 0%, #7b7645 50%, var(--wall-olive) 100%);
  }
  .stone-grain { position: absolute; inset: 0; width: 100%; height: 100%; opacity: 0.35; mix-blend-mode: overlay; }

  .running-head {
    position: absolute; top: 50px;
    font-family: "Crimson Pro", Georgia, serif; font-weight: 700;
    font-size: 21px; color: var(--header-ink);
  }
  .running-head.folio { left: 44px; }
  .running-head.title { right: 52px; }

  .frame { position: absolute; background: var(--frame-black); }
  .art, .story { position: absolute; }
  .story {
    background:
      radial-gradient(ellipse at 15% 80%, var(--parchment-teal), transparent 55%),
      radial-gradient(ellipse at 80% 15%, var(--parchment-light), transparent 60%),
      linear-gradient(160deg, var(--parchment), var(--parchment-shade));
    font-family: "Libre Baskerville", Georgia, serif;
    font-size: 15px; line-height: 20.8px; color: var(--ink);
  }
  .story p { text-indent: 24px; margin-bottom: 10px; }
  .story p.opening { text-indent: 0; }
  .drop-cap {
    float: left; font-size: 49px; line-height: 38px; font-weight: 700;
    margin: 2px 3px 0 16px;
  }

  /* Scene one */
  .frame-one-art { left: 39px; top: 122px; width: 298px; height: 416px; }
  .frame-one-text { left: 329px; top: 122px; width: 486px; height: 319px; }
  .art-corridor {
    left: 11px; top: 10px; width: 276px; height: 396px;
    background:
      radial-gradient(ellipse 90px 60px at 10% 5%, var(--scene-magenta), transparent 75%),
      radial-gradient(ellipse 120px 60px at 45% 15%, var(--scene-slate), transparent 75%),
      radial-gradient(ellipse 70px 50px at 15% 45%, var(--scene-rose), transparent 75%),
      radial-gradient(ellipse 120px 140px at 70% 55%, var(--scene-indigo), transparent 75%),
      radial-gradient(ellipse 160px 80px at 40% 88%, var(--scene-slate), transparent 75%),
      linear-gradient(160deg, var(--scene-violet) 0%, var(--scene-indigo) 45%, var(--scene-navy) 100%);
  }
  .story-one { left: 9px; top: 10px; width: 468px; height: 299px; padding: 14px 10px 0 12px; }

  /* Scene two */
  .frame-two { left: 34px; top: 574px; width: 788px; height: 450px; }
  .story-two { left: 10px; top: 10px; width: 333px; height: 430px; padding: 15px 6px 0 6px; }
  .art-guards {
    left: 353px; top: 10px; width: 425px; height: 430px;
    background:
      radial-gradient(ellipse 120px 110px at 60% 36%, var(--scene-magenta), transparent 72%),
      radial-gradient(ellipse 180px 70px at 78% 30%, var(--scene-rose), transparent 75%),
      radial-gradient(ellipse 140px 90px at 15% 12%, var(--scene-rose), transparent 75%),
      radial-gradient(ellipse 200px 60px at 55% 70%, var(--scene-slate), transparent 75%),
      radial-gradient(ellipse 140px 120px at 20% 55%, var(--scene-indigo), transparent 75%),
      linear-gradient(180deg, var(--scene-violet) 0%, var(--scene-indigo) 50%, var(--scene-navy) 100%);
  }
</style>
</head>
<body>
  <main class="page">
    <svg class="stone-grain" aria-hidden="true">
      <filter id="grain"><feTurbulence type="fractalNoise" baseFrequency="0.035 0.08" numOctaves="4" seed="7"/><feColorMatrix type="saturate" values="0"/></filter>
      <rect width="100%" height="100%" filter="url(#grain)"/>
    </svg>

    <div class="running-head folio">Page 3</div>
    <div class="running-head title">The Amber Lantern</div>

    <div class="frame frame-one-art">
      <div class="art art-corridor" role="img" aria-label="Painted view of shadowy stone dungeon corridor with carved blocks in violet and indigo"></div>
    </div>
    <div class="frame frame-one-text">
      <div class="story story-one">
        <p class="opening"><span class="drop-cap">H</span>idden in the flickering shadows, the young adventurer heard the sounds of struggle echo off the stone walls of the belly of the Palace of Seven Moons.</p>
        <p>He crept forward carefully, stepping so softly that he could listen, but he could not be heard. He had not survived so many deadly encounters in his young life by giving away his position.</p>
        <p>He heard a knife clatter to the ground, followed by an obscene laugh.</p>
        <p>He turned a corner in those dank dungeons and saw it --</p>
      </div>
    </div>

    <div class="frame frame-two">
      <div class="story story-two">
        <p>It was a gaggle of the imperial guards. He saw an arched juncture or hallway where several passages met, and dimly-lit stairs beyond; the very place he had been trying to find.</p>
        <p>He counted five men. They were close. He heard their laughter clearly now.</p>
        <p>He could not make out what they were doing until his eyes adjusted to the bright pool of light beneath the mounted torches which illuminated them. The five men had pinned a wriggling prisoner against the stone walls; now they laughed at the prisoner's vain struggles. They took turns slapping the helpless figure.</p>
        <p>A girl --</p>
      </div>
      <div class="art art-guards" role="img" aria-label="Painted scene of silhouetted palace guards beneath magenta torchlight in a stone juncture"></div>
    </div>
  </main>
</body>
</html>
```